"Giggle Garden Days" Summer Camp flyer for preschool

I need a flyer for our preschool's summer camp. Our summer theme is GIGGLE garden DAYS. the theme MUST be displayed. We would like a mad scientist with crazy hair look with test tubes and goggles PROMINENTLY DISPLAYED on the flyer. this is for a preschool so we don't want the scientist to look scary. Our logo needs to be included on the flyer. The age range for the school is 6weeks to 6 years (you can add "6 weeks to 6 years" somewhere small on the flyer). Please add "Camp starts June 5th" and Sign up for 1 camp or all!". The weekly themes for the camp are ...
Journey into Outer Space
Rock Out in Geology
Weather
Water Extravagnaza
Biology
Physics - Force & Motion
Light
Sensational Sounds
Budding Builders
Krazy Kitchen Chemistry
Electromagnetism
It's Hip to Be Healthy
we don't want these on the flyer but maybe you can use them for image inspiration.
Attached is our logo and some verbiage that can be used.

moms and dads of preschool age kids

Preschool

• our logo, title of the camp, dates, a Mad Scientist with crazy hair, test tube, and goggles. attached is image of scientist. i will purchase this once art is approved.
• it would be nice to have the weekly themes on the flyer

```html
<!DOCTYPE html>
<html lang="en">
<head>
<meta charset="utf-8">
<title>Giggle Garden Days – Summer Camp Flyer</title>
<link href="https://fonts.googleapis.com/css2?family=Bangers&family=Gochi+Hand&family=Caveat:wght@400;700&display=swap" rel="stylesheet">
<style>
  :root {
    --plum: #5b1e3a;
    --brick: #a8321f;
    --orange: #e2702a;
    --amber: #f2b548;
    --cream: #fbf1d2;
    --yellow: #ffd21a;
    --gold: #f29a0c;
    --ink: #141414;
    --navy: #1c2a6b;
    --silver: #d9dbe2;
    --silver-dark: #9da1ad;
    --white: #ffffff;
    --dash: #c9c2b0;
  }
  html, body {
    margin: 0;
    padding: 0;
    width: 921px;
    height: 1200px;
    overflow: hidden;
    background: var(--cream);
  }
  .flyer {
    position: relative;
    width: 921px;
    height: 1200px;
    overflow: hidden;
    background: linear-gradient(165deg, var(--plum) 0%, var(--brick) 28%, var(--orange) 46%, var(--amber) 66%, var(--cream) 88%);
    font-family: "Caveat", cursive;
  }
  .camp-label {
    position: absolute;
    left: 36px;
    top: 84px;
    margin: 0;
    font-family: "Gochi Hand", cursive;
    font-weight: 400;
    font-size: 62px;
    line-height: 0.95;
    color: var(--white);
    transform: rotate(-6deg);
    text-shadow: 2px 2px 0 rgba(0,0,0,0.35);
  }
  .camp-label .second-line { display: block; padding-left: 42px; }
  .sun-art {
    position: absolute;
    left: 250px;
    top: 92px;
    width: 128px;
    height: 128px;
    border-radius: 50%;
    background: radial-gradient(circle, var(--yellow) 55%, var(--gold) 100%);
  }
  .scientist-art {
    position: absolute;
    left: 440px;
    top: 40px;
    width: 400px;
    height: 740px;
    border-radius: 40px;
    background: linear-gradient(180deg, #cfd3d6 0%, #a9c9cf 45%, #2a2a2a 100%);
    opacity: 0.85;
  }
  .burst-art {
    position: absolute;
    left: 70px;
    top: 340px;
    width: 360px;
    height: 280px;
    background: radial-gradient(ellipse at center, var(--yellow) 0%, var(--gold) 45%, rgba(242,154,12,0) 72%);
  }
  .camp-title {
    position: absolute;
    left: 110px;
    top: 450px;
    margin: 0;
    font-family: "Bangers", cursive;
    font-weight: 400;
    line-height: 0.85;
    transform: rotate(-6deg);
    transform-origin: left center;
  }
  .camp-title span { display: block; paint-order: stroke fill; -webkit-text-stroke: 8px var(--ink); }
  .title-giggle { font-size: 112px; color: var(--yellow); letter-spacing: 2px; }
  .title-garden { font-size: 42px; color: var(--white); padding-left: 140px; -webkit-text-stroke: 6px var(--ink) !important; }
  .title-days { font-size: 118px; color: var(--white); letter-spacing: 4px; }
  .date-banner {
    position: absolute;
    left: 100px;
    top: 745px;
    width: 470px;
    padding: 8px 22px 10px;
    background: linear-gradient(180deg, var(--white) 0%, var(--silver) 55%, var(--silver-dark) 100%);
    box-shadow: 4px 6px 10px rgba(0,0,0,0.3);
    transform: rotate(-9deg);
  }
  .date-range {
    margin: 0;
    font-weight: 700;
    font-size: 56px;
    line-height: 1;
    color: var(--ink);
    white-space: nowrap;
  }
  .age-range {
    margin: 2px 0 0;
    font-size: 22px;
    line-height: 1.1;
    color: var(--navy);
    white-space: nowrap;
  }
  .weekly-themes {
    position: absolute;
    left: 146px;
    top: 912px;
    width: 690px;
    transform: rotate(-4deg);
    transform-origin: left top;
  }
  .themes-heading {
    margin: 0 0 6px;
    font-size: 28px;
    font-weight: 700;
    color: var(--navy);
  }
  .theme-row {
    list-style: none;
    margin: 0 0 8px;
    padding: 0;
    display: flex;
    gap: 10px;
  }
  .theme-row li {
    border: 2px dashed var(--dash);
    padding: 0 10px;
    font-size: 26px;
    line-height: 1.4;
    color: var(--ink);
    white-space: nowrap;
  }
  .theme-row li.bold { font-weight: 700; }
  .logo-slot {
    position: absolute;
    left: 752px;
    top: 948px;
    width: 130px;
    height: 140px;
    border-radius: 10px;
    background: var(--white);
    display: flex;
    align-items: center;
    justify-content: center;
    text-align: center;
    font-size: 18px;
    line-height: 1.2;
    color: #a8a8a8;
    transform: rotate(-3deg);
  }
</style>
</head>
<body>
<main class="flyer">
  <h2 class="camp-label">Summer<span class="second-line">Camp</span></h2>
  <div class="sun-art" role="img" aria-label="Smiling cartoon sun"></div>
  <div class="scientist-art" role="img" aria-label="Friendly cartoon mad scientist with wild white hair, goggles, lab coat and test tubes"></div>
  <div class="burst-art" role="img" aria-label="Comic explosion burst with puffs of smoke"></div>
  <h1 class="camp-title">
    <span class="title-giggle">GIGGLE</span>
    <span class="title-garden">garden</span>
    <span class="title-days">DAYS</span>
  </h1>
  <div class="date-banner">
    <p class="date-range">June 5th – August 28th</p>
    <p class="age-range">The age range for the school is 6weeks to 6 years</p>
  </div>
  <section class="weekly-themes">
    <h3 class="themes-heading">The weekly themes for the camp are :</h3>
    <ul class="theme-row">
      <li>Journey into Outer Space</li>
      <li>Physics – Force &amp; Motion</li>
      <li>It's Hip to Be Healthy</li>
    </ul>
    <ul class="theme-row">
      <li>Rock Out in Geology</li>
      <li>Biology</li>
      <li class="bold">Light</li>
      <li class="bold">Budding Builders</li>
    </ul>
    <ul class="theme-row">
      <li>Weather</li>
      <li>Water Extravagnaza</li>
      <li>Sensational Sounds</li>
    </ul>
    <ul class="theme-row">
      <li>Krazy Kitchen Chemistr</li>
      <li>Electromagnetism</li>
    </ul>
  </section>
  <div class="logo-slot">Logo<br>Place holder</div>
</main>
</body>
</html>
```